Flyer design needed for fancy dress website.

We are looking for a flyer design that advertises our fancy dress website www.brumzo.co.uk. The flyer needs to be A6 size and must be front and back.
Target Market(s)
Fancy dress goers and students.
Requirements
Must have
- The flyer must have the www.brumzo.co.uk logo and telephone number 02079461382 standing out on the flyer. Also the promotional code "frost47" giving you 10% off your order when you shop online. A modern twist with similar lettering to the www.brumzo.co.uk logo is a must. Needs to include that the item is made out of a fleece material and is very warm and cosy perfect for winter. Needs to include that there is a huge range of animal costumes.
Nice to have
- I would like to see some of the pictures of people in the costumes in the backgroud behind the website address, telephone number and the promotional code. Also the slogan 'the best onesies money can buy' accross the bottom would be good. Also an ilistration of a person modeling the costume would be good.

```html
<!DOCTYPE html>
<html lang="en">
<head>
<meta charset="utf-8">
<title>Brumzo flyer – front and back</title>
<link href="https://fonts.googleapis.com/css2?family=Chewy&family=Patrick+Hand&display=swap" rel="stylesheet">
<style>
  :root {
    --bg: #ece8e2;
    --paper: #ffffff;
    --ink-blue: #34399a;
    --red: #e2362c;
    --green: #3aa845;
    --orange: #f7941d;
    --badge-ink: #1d1d1d;
    --shadow: rgba(0,0,0,0.28);
  }
  html, body {
    margin: 0;
    padding: 0;
    width: 1200px;
    height: 848px;
    overflow: hidden;
    background: var(--bg);
    font-family: "Chewy", "Patrick Hand", "Comic Sans MS", "Chalkboard SE", "Comic Neue", cursive;
  }
  .canvas { position: relative; width: 1200px; height: 848px; }
  .flyer {
    position: absolute;
    width: 440px;
    height: 610px;
    background: var(--paper);
    box-shadow: 4px 6px 14px var(--shadow);
    overflow: hidden;
  }
  .flyer--front { left: 130px; top: 90px; }
  .flyer--back  { left: 630px; top: 150px; }

  .brand-name {
    position: absolute;
    left: 0; right: 0;
    margin: 0;
    text-align: center;
    color: var(--ink-blue);
    font-weight: 400;
    letter-spacing: 3px;
    white-space: nowrap;
  }
  .mascots {
    position: absolute;
    border-radius: 10px;
    background: linear-gradient(90deg, #f2e23a 0 50%, #e9e9e9 50%, #cfcfcf 100%);
  }

  /* Front */
  .flyer--front .brand-name { top: 20px; font-size: 30px; }
  .flyer--front .mascots { left: 175px; top: 62px; width: 90px; height: 84px; }
  .slogan {
    position: absolute;
    left: 0; right: 0; top: 154px;
    margin: 0;
    text-align: center;
    color: var(--ink-blue);
    font-size: 17px;
    letter-spacing: 1.5px;
    white-space: nowrap;
  }
  .costume-ring {
    position: absolute;
    left: 45px; top: 180px;
    width: 360px; height: 360px;
    border-radius: 50%;
    background: radial-gradient(circle, var(--paper) 0 27%, #f3c7d6 28%, #c99a6a 46%, #6e6a9e 62%, #e8e8e8 71%, var(--paper) 72%);
  }
  .promo-centre {
    position: absolute;
    left: 0; right: 0; top: 318px;
    text-align: center;
    line-height: 1.2;
  }
  .promo-centre .word { display: block; color: var(--red); font-size: 32px; letter-spacing: 3px; }
  .promo-centre .num  { display: block; color: var(--green); font-size: 32px; letter-spacing: 3px; }
  .range-note {
    position: absolute;
    left: 0; right: 0; top: 558px;
    margin: 0;
    text-align: center;
    color: var(--ink-blue);
    font-size: 20px;
    letter-spacing: 1.5px;
    white-space: nowrap;
  }

  /* Back */
  .flyer--back .brand-name { top: 24px; font-size: 24px; }
  .flyer--back .mascots { left: 190px; top: 60px; width: 62px; height: 66px; }
  .model-photo {
    position: absolute;
    left: 30px; top: 135px;
    width: 300px; height: 360px;
    background: linear-gradient(160deg, #e8c4e8 0%, #f2a4c4 30%, #d82a26 55%, #c21f1f 80%, #f4f1ee 100%);
  }
  .fleece-badge { position: absolute; left: 298px; top: 130px; width: 128px; height: 128px; }
  .fleece-badge svg { display: block; }
  .fleece-badge p {
    position: absolute;
    inset: 0;
    margin: 0;
    display: flex; align-items: center; justify-content: center;
    text-align: center;
    font-size: 12px;
    line-height: 1.2;
    color: var(--badge-ink);
    padding: 0 22px;
  }
  .promo-sign {
    position: absolute;
    left: 98px; top: 262px;
    width: 250px; height: 136px;
    background: #f7f7f7;
    border: 1px solid #bdbdbd;
    box-shadow: 1px 2px 4px rgba(0,0,0,0.2);
    text-align: center;
  }
  .promo-sign .code { margin: 8px 0 0; font-size: 24px; line-height: 1.1; letter-spacing: 2px; }
  .promo-sign .code .word { color: var(--red); }
  .promo-sign .code .num { color: var(--green); }
  .promo-sign .rule { height: 3px; background: var(--red); margin: 4px 14px 2px; }
  .promo-sign .discount { margin: 0; color: var(--red); font-size: 42px; line-height: 1.05; letter-spacing: 2px; }
  .promo-sign .cta { margin: 2px 0 0; color: var(--green); font-size: 24px; line-height: 1.1; letter-spacing: 3px; }
  .web-address {
    position: absolute; left: 0; right: 0; top: 510px;
    margin: 0; text-align: center;
    color: var(--ink-blue); font-size: 32px; letter-spacing: 2px;
    white-space: nowrap;
  }
  .phone {
    position: absolute; left: 0; right: 0; top: 556px;
    margin: 0; text-align: center;
    color: var(--orange); font-size: 28px; letter-spacing: 3px;
    white-space: nowrap;
  }
</style>
</head>
<body>
<main class="canvas">

  <section class="flyer flyer--front" aria-label="Flyer front">
    <h1 class="brand-name">BRUMZO.CO.UK</h1>
    <div class="mascots" role="img" aria-label="Illustrated tiger and cow mascots holding hands"></div>
    <p class="slogan">THE BEST ONESIES MONEY CAN BUY</p>
    <div class="costume-ring" role="img" aria-label="Circle of people lying in animal onesies: penguin, bear, giraffe, dinosaur, unicorn, fox, chicken, koala, skeleton, tiger, pig and monkey"></div>
    <div class="promo-centre">
      <span class="word">FROST</span>
      <span class="num">47</span>
    </div>
    <p class="range-note">HUGE RANGE OF ANIMAL COSTUMES</p>
  </section>

  <section class="flyer flyer--back" aria-label="Flyer back">
    <h2 class="brand-name">BRUMZO.CO.UK</h2>
    <div class="mascots" role="img" aria-label="Illustrated tiger and cow mascots holding hands"></div>
    <div class="model-photo" role="img" aria-label="Man in a red Santa onesie holding a sign, with friends in pastel bear onesies behind him"></div>

    <div class="fleece-badge">
      <svg width="128" height="128" viewBox="0 0 130 130" aria-hidden="true">
        <polygon fill="#f7941d" points="65,2 74,17 89,6 92,24 110,19 106,37 124,40 113,55 128,65 113,75 124,90 106,93 110,111 92,106 89,124 74,113 65,128 56,113 41,124 38,106 20,111 24,93 6,90 17,75 2,65 17,55 6,40 24,37 20,19 38,24 41,6 56,17"/>
      </svg>
      <p>MADE OF FLEECE WARM AND COSY PERFECT FOR WINTER</p>
    </div>

    <div class="promo-sign">
      <p class="code"><span class="word">FROST</span> <span class="num">47</span></p>
      <div class="rule"></div>
      <p class="discount">10% OFF</p>
      <p class="cta">SHOP ONLINE</p>
    </div>

    <p class="web-address">WWW.BRUMZO.CO.UK</p>
    <p class="phone">02079461382</p>
  </section>

</main>
</body>
</html>
```